Hold Your Breath Events Business Card Design

I provide event planning for surprise parties, celebrating all types of life events, such as birthdays, graduations, promotions, baby showers, bridal showers, grandparent showers, health (cancer survivor), wedding anniversary etc.

I would like to see designs that show that we are fun, creative, whimical, yet professional. I am not too fond of clip art, open to all shorts of fonts and graphics, especially photos of people that appear to be saying "shh" or people being surprised.

I am open to all colors, and was considering having the same logo/business card done in different color schemes that match the occasion/client such as bright colors for a birthday, silver, gold for anniversary, pastels for a baby related party or an older person's birthday.

I would like to have the word Surprise be very bold, and stick out from the rest of the lettering..almost like people are shouting "surprise" to the honoree.

Industry/Entity Type

Event Planning

Contact Information for Business Card

Hold Your Breath Events!
D Harlowe President/Owner
www.holdbreathevents.example
dharlowe@holdbreathevents.example
555 318 2947
4716 Maple Hollow Rd
Brookmere Falls PA 19999

```html
<!DOCTYPE html>
<html lang="en">
<head>
<meta charset="utf-8">
<title>Hold Your Breath Events – Business Card</title>
<link rel="stylesheet" href="https://fonts.googleapis.com/css2?family=Mulish:wght@700&family=Questrial&display=swap">
<style>
  :root {
    --backdrop: #2b2b2b;
    --card-light: #f6e7bd;
    --card-mid: #efdcaa;
    --card-deep: #e6cf96;
    --gold: #b8862a;
    --gold-dark: #8c6418;
    --ink: #2a2418;
    --name-brown: #4a3410;
  }
  * { margin: 0; padding: 0; box-sizing: border-box; }
  html, body {
    width: 1200px;
    height: 660px;
    overflow: hidden;
    background: var(--backdrop);
  }
  .canvas {
    position: relative;
    width: 1200px;
    height: 660px;
    display: flex;
    align-items: center;
    justify-content: center;
  }
  .business-card {
    position: relative;
    width: 980px;
    height: 560px;
    background: linear-gradient(120deg, var(--card-mid) 0%, var(--card-light) 45%, var(--card-deep) 100%);
    box-shadow: 0 18px 40px rgba(0,0,0,0.45);
    font-family: "Questrial", sans-serif;
    color: var(--ink);
    overflow: hidden;
  }
  .hush {
    position: absolute;
    left: 48px;
    top: 86px;
    font-size: 44px;
    letter-spacing: 1px;
    color: var(--ink);
  }
  .brand-name {
    position: absolute;
    left: 150px;
    top: 170px;
    width: 320px;
    font-size: 40px;
    line-height: 1.15;
    color: var(--ink);
  }
  .ornament {
    position: absolute;
    right: 60px;
    top: 0;
    width: 330px;
    height: 250px;
    border-radius: 0 0 40% 60%;
    background: radial-gradient(ellipse at 55% 40%, #c99a3a 0%, var(--gold) 45%, rgba(184,134,42,0.25) 80%, rgba(184,134,42,0) 100%);
  }
  .owner {
    position: absolute;
    right: 48px;
    top: 268px;
    text-align: right;
  }
  .owner-name {
    font-family: "Mulish", sans-serif;
    font-weight: 700;
    font-size: 44px;
    color: var(--name-brown);
    line-height: 1.1;
  }
  .owner-title {
    font-size: 26px;
    color: var(--name-brown);
    margin-top: 2px;
  }
  .owner-address {
    font-size: 22px;
    color: var(--ink);
    margin-top: 18px;
  }
  .contact-list {
    position: absolute;
    left: 48px;
    top: 368px;
    list-style: none;
    font-size: 22px;
    line-height: 38px;
  }
  .contact-list li {
    display: flex;
    align-items: center;
    gap: 12px;
    white-space: nowrap;
  }
  .contact-icon {
    width: 18px;
    height: 18px;
    flex: none;
    fill: var(--ink);
  }
</style>
</head>
<body>
<main class="canvas">
  <article class="business-card">
    <p class="hush">shh...</p>

    <h1 class="brand-name">Hold Your Breath Events!</h1>

    <div class="ornament" role="img" aria-label="Gold flourish ornament with curling scrolls"></div>

    <section class="owner">
      <p class="owner-name">D Harlowe</p>
      <p class="owner-title">President/Owner</p>
      <p class="owner-address">4716 Maple Hollow Rd Brookmere Falls PA 19999</p>
    </section>

    <ul class="contact-list">
      <li>
        <svg class="contact-icon" viewBox="0 0 24 24" aria-hidden="true"><path d="M6.6 10.8a15.1 15.1 0 0 0 6.6 6.6l2.2-2.2c.3-.3.7-.4 1-.2 1.1.4 2.3.6 3.6.6.6 0 1 .4 1 1V20c0 .6-.4 1-1 1A17 17 0 0 1 3 4c0-.6.4-1 1-1h3.5c.6 0 1 .4 1 1 0 1.3.2 2.5.6 3.6.1.3 0 .7-.2 1z"/></svg>
        <span>555 318 2947</span>
      </li>
      <li>
        <svg class="contact-icon" viewBox="0 0 24 24" aria-hidden="true"><circle cx="12" cy="12" r="10" fill="none" stroke="currentColor" stroke-width="2" style="stroke:var(--ink)"/><path d="M2 12h20M12 2c3 3 3 17 0 20M12 2c-3 3-3 17 0 20" fill="none" style="stroke:var(--ink)" stroke-width="1.6"/></svg>
        <span>dharlowe@holdbreathevents.example</span>
      </li>
      <li>
        <svg class="contact-icon" viewBox="0 0 24 24" aria-hidden="true"><path d="M2 5h20v14H2z"/><path d="M2 5l10 8 10-8" fill="none" stroke="#efdcaa" stroke-width="1.6"/></svg>
        <span>www.holdbreathevents.example</span>
      </li>
      <li>
        <svg class="contact-icon" viewBox="0 0 24 24" aria-hidden="true"><circle cx="12" cy="12" r="9"/></svg>
        <span>@dharlowe</span>
      </li>
    </ul>
  </article>
</main>
</body>
</html>
```